Postcard for commercial concrete cleaning company that will be mailed to business customers

A 6x9 postcard that will be mailed out to businesses who have concrete (sidewalks, drive thrus, dumpster pads, etc) that need periodic pressure washing to keep clean. Our current customers are majority restaurants. We are able to remove gum and grease from concrete which is difficult for much of our competitors. We work at night when the businesses are closed or slow if 24hr.

Target Market(s)

This will go to restaurants, banks, gas stations and other retail locations.

Colors

Designer to choose colors to be used in the design.

Requirements
Must have
• Logo. A headline that mentions commercial concrete cleaning so recipients will know at a glance what we do
Nice to have
• The image included is of a fast food doorway that is half cleaned, the right side. Something like "Dirty Doorway?" may make sense.
• We specialize is maintenance concrete cleaning where we come on a regular basis so I like phrase keep your concrete clean, or keep your business clean. something like that.

```html
<!DOCTYPE html>
<html lang="en">
<head>
<meta charset="utf-8">
<title>Ridgeline Commercial Pressure Washing — Postcard</title>
<link rel="stylesheet" href="https://fonts.googleapis.com/css2?family=Source+Sans+3:wght@300;400;600;700;900&display=swap">
<style>
  :root {
    --navy: #0d2f6e;
    --blue: #1356a8;
    --royal: #1e64c0;
    --sky: #35b6ea;
    --ink: #111827;
    --white: #ffffff;
    --page: #e6e7e9;
    --photo-light: #e9e4dc;
    --photo-mid: #b9b1a4;
    --photo-dark: #6f655b;
  }
  * { box-sizing: border-box; margin: 0; padding: 0; }
  html, body {
    width: 933px; height: 1200px; overflow: hidden;
    background: var(--page);
    font-family: "Source Sans 3", Arial, sans-serif;
  }
  .card {
    position: absolute; left: 73px; width: 789px; height: 526px;
    background: var(--white); overflow: hidden;
    box-shadow: 0 4px 14px rgba(0,0,0,.25);
  }
  .card--front { top: 51px; }
  .card--back { top: 611px; }
  .card__art { position: absolute; inset: 0; width: 100%; height: 100%; }
  .abs { position: absolute; }

  /* Front */
  .headline {
    left: 0; width: 789px; top: 18px; text-align: center;
    font-weight: 900; font-size: 52px; line-height: 1; letter-spacing: -.5px;
    color: var(--blue); text-shadow: 0 2px 4px rgba(0,0,0,.35);
  }
  .subhead {
    left: 0; width: 789px; top: 80px; text-align: center;
    font-weight: 700; font-size: 21px; color: var(--ink);
  }
  .wordmark { color: var(--navy); font-weight: 600; line-height: 1; }
  .wordmark__name { display: block; font-size: 38px; letter-spacing: -.3px; }
  .wordmark__tag { display: block; font-size: 26px; letter-spacing: 6.4px; margin-top: 10px; }
  .front-logo { left: 18px; top: 400px; }
  .specialty { left: 20px; top: 489px; font-size: 14px; font-weight: 700; color: var(--ink); }
  .front-cta {
    right: 10px; top: 453px; font-size: 14px; font-weight: 700; color: var(--ink);
  }
  .phone-pill {
    left: 482px; top: 471px; width: 320px; height: 39px;
    background: linear-gradient(90deg, var(--navy), var(--blue));
    border-radius: 20px 0 0 20px;
    display: flex; align-items: center; gap: 10px; padding-left: 34px;
    color: var(--white); font-size: 31px; font-weight: 600; letter-spacing: 2px;
  }
  .icon-phone { width: 27px; height: 27px; flex: none; }

  /* Back */
  .intro {
    left: 24px; top: 43px; width: 430px;
    color: var(--white); font-weight: 700; font-size: 21px; line-height: 26px;
  }
  .tab {
    left: 0; top: 147px; width: 274px; height: 43px;
    background: linear-gradient(180deg, #fff, #e4e6ea);
    border-radius: 0 22px 22px 0; box-shadow: 2px 3px 5px rgba(0,0,0,.35);
    padding-left: 24px; display: flex; align-items: center;
    font-size: 27px; font-weight: 400; color: var(--ink);
  }
  .about {
    left: 25px; top: 208px; width: 410px;
    color: var(--white); font-size: 14.5px; line-height: 17px;
  }
  .services { left: 25px; top: 273px; list-style: none; }
  .services li {
    display: flex; align-items: center; gap: 10px; height: 24px;
    color: var(--white); font-weight: 700; font-size: 17px;
  }
  .tick { width: 16px; height: 16px; flex: none; }
  .phone-strip {
    left: 0; top: 401px; width: 340px; height: 70px;
    background: linear-gradient(90deg, #fff 60%, #d9dce1);
    display: flex; align-items: center; gap: 10px; padding-left: 24px;
    font-size: 31px; font-weight: 600; letter-spacing: 2px; color: var(--ink);
  }
  .back-cta { left: 25px; top: 485px; color: var(--white); font-weight: 700; font-size: 16px; }
  .stamp { left: 662px; top: 33px; width: 106px; height: 65px; border: 1.5px solid #b9bcc2; }
  .address-line { left: 474px; width: 290px; height: 0; border-top: 1.5px solid #c4c7cc; }
  .back-logo { left: 442px; top: 418px; }
  .back-logo .wordmark__name { font-size: 36px; }
  .back-logo .wordmark__tag { font-size: 25px; letter-spacing: 6px; }
</style>
</head>
<body>

<section class="card card--front">
  <svg class="card__art" viewBox="0 0 900 600" preserveAspectRatio="none" aria-hidden="false">
    <defs>
      <linearGradient id="photoTone" x1="0" y1="0" x2="1" y2="1">
        <stop offset="0" stop-color="#8a8075"/>
        <stop offset=".35" stop-color="#e9e4dc"/>
        <stop offset=".7" stop-color="#cfc7ba"/>
        <stop offset="1" stop-color="#a89a86"/>
      </linearGradient>
      <linearGradient id="circleA" x1="0" y1="0" x2="1" y2="0">
        <stop offset="0" stop-color="#b5847c"/><stop offset="1" stop-color="#5f5a52"/>
      </linearGradient>
      <linearGradient id="circleB" x1="0" y1="0" x2="1" y2="1">
        <stop offset="0" stop-color="#6d6760"/><stop offset="1" stop-color="#c9c4bd"/>
      </linearGradient>
      <linearGradient id="circleC" x1="0" y1="0" x2="1" y2="1">
        <stop offset="0" stop-color="#4b5866"/><stop offset="1" stop-color="#e3e5e6"/>
      </linearGradient>
      <linearGradient id="bandNavy" x1="0" x2="1">
        <stop offset="0" stop-color="#0d2f6e"/><stop offset="1" stop-color="#1e64c0"/>
      </linearGradient>
    </defs>
    <rect role="img" aria-label="Photo of a worker pressure washing a concrete walkway at a business doorway, half cleaned" x="0" y="0" width="900" height="480" fill="url(#photoTone)"/>
    <path d="M0,400 C180,320 380,330 520,400 C650,470 780,470 900,410 L900,460 C780,500 640,500 520,440 C380,370 180,360 0,430Z" fill="#35b6ea"/>
    <path d="M0,380 C150,320 250,320 300,330 C200,330 100,360 0,410Z" fill="url(#bandNavy)"/>
    <path d="M0,395 C180,335 380,345 520,415 C650,480 780,480 900,430 L900,600 L0,600Z" fill="#fff"/>
    <path d="M650,470 C750,490 830,470 900,440 L900,470 C820,500 740,500 650,470Z" fill="#1356a8"/>
    <g stroke="#1356a8" stroke-width="5">
      <circle role="img" aria-label="Close-up of brick paving before and after cleaning" cx="295" cy="334" r="69" fill="url(#circleA)"/>
      <circle role="img" aria-label="Close-up of a pressure washer nozzle spraying concrete" cx="482" cy="390" r="69" fill="url(#circleB)"/>
      <circle role="img" aria-label="Close-up of stained concrete next to a cleaned section" cx="665" cy="425" r="69" fill="url(#circleC)"/>
    </g>
  </svg>

  <h1 class="abs headline">DIRTY DOORWAY?</h1>
  <p class="abs subhead">- KEEP YOUR BUSINESS CLEAN -</p>

  <div class="abs wordmark front-logo">
    <span class="wordmark__name">Ridgeline Commercial</span>
    <span class="wordmark__tag">PRESSURE WASHING</span>
  </div>
  <p class="abs specialty">WE SPECIALIZE IS MAINTENANCE CONCRETE CLEANING</p>

  <p class="abs front-cta">CALL US NOW FOR A FREE ESTIMATE!</p>
  <div class="abs phone-pill">
    <svg class="icon-phone" viewBox="0 0 24 24" fill="none" stroke="currentColor" stroke-width="2">
      <circle cx="12" cy="12" r="10.5"/>
      <path d="M8.2 6.5l1.9 2.6-1 1.4c.7 1.6 1.9 2.8 3.5 3.5l1.4-1 2.6 1.9-.9 2c-4.6-.3-8.6-4.3-8.9-8.9z" fill="currentColor" stroke="none"/>
    </svg>
    <span>(555) 014-2290</span>
  </div>
</section>

<section class="card card--back">
  <svg class="card__art" viewBox="0 0 900 600" preserveAspectRatio="none" aria-hidden="true">
    <defs>
      <linearGradient id="panelBlue" x1="0" y1="0" x2="1" y2="1">
        <stop offset="0" stop-color="#1356a8"/><stop offset=".6" stop-color="#0d2f6e"/><stop offset="1" stop-color="#0b2760"/>
      </linearGradient>
    </defs>
    <path d="M520,0 L570,0 C630,140 580,260 505,370 C440,470 430,540 480,600 L420,600 C380,520 410,430 470,340 C540,230 570,120 520,0Z" fill="#35b6ea"/>
    <path d="M0,0 L530,0 C575,120 545,230 475,340 C415,440 390,520 420,600 L0,600Z" fill="#1e64c0"/>
    <path d="M0,0 L515,0 C558,120 528,225 460,335 C400,435 375,520 400,600 L0,600Z" fill="url(#panelBlue)"/>
    <rect x="0" y="537" width="400" height="63" fill="#1356a8"/>
  </svg>

  <p class="abs intro">Ridgeline Commercial Pressure Washing, is a maintenance concrete cleaning &amp; pressure washing company.</p>

  <div class="abs tab">PRESSURE WASHING</div>

  <p class="abs about">We are able to remove gum and grease from concrete which is difficult for much of our competitors. We work at night when the businesses are closed or slow if 24hr.</p>

  <ul class="abs services">
    <li><svg class="tick" viewBox="0 0 16 16"><circle cx="8" cy="8" r="8" fill="#fff"/><path d="M4.3 8.3l2.4 2.3 5-5" fill="none" stroke="#0d2f6e" stroke-width="2"/></svg>SIDEWALKS</li>
    <li><svg class="tick" viewBox="0 0 16 16"><circle cx="8" cy="8" r="8" fill="#fff"/><path d="M4.3 8.3l2.4 2.3 5-5" fill="none" stroke="#0d2f6e" stroke-width="2"/></svg>DRIVE THRUS</li>
    <li><svg class="tick" viewBox="0 0 16 16"><circle cx="8" cy="8" r="8" fill="#fff"/><path d="M4.3 8.3l2.4 2.3 5-5" fill="none" stroke="#0d2f6e" stroke-width="2"/></svg>DUMPSTER PADS</li>
    <li><svg class="tick" viewBox="0 0 16 16"><circle cx="8" cy="8" r="8" fill="#fff"/><path d="M4.3 8.3l2.4 2.3 5-5" fill="none" stroke="#0d2f6e" stroke-width="2"/></svg>CONCRETE CLEANING</li>
    <li><svg class="tick" viewBox="0 0 16 16"><circle cx="8" cy="8" r="8" fill="#fff"/><path d="M4.3 8.3l2.4 2.3 5-5" fill="none" stroke="#0d2f6e" stroke-width="2"/></svg>AND MUCH MORE</li>
  </ul>

  <div class="abs phone-strip">
    <svg class="icon-phone" viewBox="0 0 24 24" fill="none" stroke="currentColor" stroke-width="2">
      <circle cx="12" cy="12" r="10.5"/>
      <path d="M8.2 6.5l1.9 2.6-1 1.4c.7 1.6 1.9 2.8 3.5 3.5l1.4-1 2.6 1.9-.9 2c-4.6-.3-8.6-4.3-8.9-8.9z" fill="currentColor" stroke="none"/>
    </svg>
    <span>(555) 014-2290</span>
  </div>
  <p class="abs back-cta">CALL US NOW FOR A FREE ESTIMATE!</p>

  <div class="abs stamp"></div>
  <div class="abs address-line" style="top:179px"></div>
  <div class="abs address-line" style="top:226px"></div>
  <div class="abs address-line" style="top:273px"></div>
  <div class="abs address-line" style="top:320px"></div>

  <div class="abs wordmark back-logo">
    <span class="wordmark__name">Ridgeline Commercial</span>
    <span class="wordmark__tag">PRESSURE WASHING</span>
  </div>
</section>

</body>
</html>
```